Security Company Needs a Website *

We need a website that gives our clients information about the services we provide, methods of contacting us and landing page to advertise on social media sites.

We need five landing pages titled Home, About Us, Services, Contact Us and a Landing Page that can be linked to Chatterlane advertising.

About Us - Should have a section for Core Values & Ethics, Our Vision, Our Mission and Partners.

Services - This page should show the different categories which include CCTV, Security Alarms, Access Control and Fire Protection.

CCTV Service Description:
Closed circuit television (CCTV) has long been implemented by businesses as a surveillance tool in areas that need monitoring. With digital CCTV cameras, multiple video cameras transmit signals through a set of monitors. The cameras provide thorough surveillance of the area.

With vast technological improvements over the last ten years, businesses with CCTV systems can use unique IP cameras and video analytics to monitor traffic flows, people-count, implement facial and number plate recognition. Useful information about customer behaviour and demographics can be discovered too. CCTV helps prevent crime in many industries and can assist with the improvement of industrial processes, safety on transport systems and traffic monitoring.

Security Alarms Service Description:
Alarms systems are electronic devices programmed to alert people to specific dangers and detect intrusions, fire or theft. Security alarms, systems and access control monitoring combine to create an integrated surveillance solution, tailored to your business’ unique requirements. Our surveillance and alarm monitoring services are ideal for perimeter protection from unwanted intruders or potential dangers.

Access Control Services:
An access control system allows for the free flow of authorised personnel while denying entry to unwanted visitors. With walk-in thieves and trespassers shut out, you dramatically reduce your exposure to crime while increasing the security of your employees, visitors, information and assets.

* Control when and who is entering your premises
* Protect employees, assets and information
* Secure an area or sector
* Observe movement
* Integrate with other security systems

Our range of access control systems can be seamlessly linked to other systems in our portfolio. These include Fire Detection Systems, Intruder Alarms, CCTV, and Building Management. A common request involves the need for a CCTV camera to pan around and focus on a door that has been highlighted as a security risk by the access control system.

Fire Protection Service:
To Be Advised

The above copy-writing will also have to be changed.

Contact Us - This form needs to be simple and straightforward to gather the prospects information and we would like to have a call to action on this page. The Contact Us page should also have a wayfindr plot location of our office address.

We would also like to have a link to our chatterlane page on the website.

Target Market(s)

Commercial businesses, building construction developers and property managers.

Industry/Entity Type

Security

Number of Pages Required

5+ page

Font styles to use
Sans Serif

Colors

Designer to choose colors to be used in the design.

Requirements
Must have
• We need to have the same look and feel as well as website features as the following website:
• https://www.kovrangard.com.au/business-security/
• The website must be easy to use and easy to edit as well.

```html
<!DOCTYPE html>
<html lang="en">
<head>
<meta charset="utf-8">
<title>Sentravia Security</title>
<link rel="stylesheet" href="https://fonts.googleapis.com/css2?family=Open+Sans:wght@400;600;700&family=Raleway:wght@500;600&display=swap">
<style>
:root{
  --blue:#1f5fae;
  --blue-dark:#1a4d8f;
  --navy:#0f2a4a;
  --charcoal:#1d1f22;
  --ink:#333;
  --muted:#777;
  --line:#cfd6df;
  --white:#fff;
  --sky-top:#2f6fc2;
  --sky-bottom:#bcd6ef;
}
*{box-sizing:border-box;margin:0;padding:0}
html,body{width:1200px;height:2344px;overflow:hidden}
body{font-family:"Open Sans",sans-serif;color:var(--ink);background:var(--white);position:relative}

.site-header{position:absolute;left:0;top:0;width:1200px;height:80px;background:var(--white);box-shadow:0 2px 6px rgba(0,0,0,.08);z-index:2}
.brand{position:absolute;left:120px;top:6px;width:120px;text-align:center}
.brand-mark{width:50px;height:50px;border-radius:50%;background:var(--navy);margin:0 auto}
.brand-name{font-size:9px;font-weight:700;color:var(--navy);margin-top:3px;letter-spacing:.3px;white-space:nowrap}
.main-nav{position:absolute;left:310px;top:30px;display:flex;gap:30px}
.main-nav a{font-size:13px;font-weight:600;color:var(--navy);text-decoration:none;letter-spacing:.5px}
.main-nav a.active{color:var(--blue);border-bottom:2px solid var(--blue);padding-bottom:4px}
.header-contact{position:absolute;right:110px;top:30px;font-size:13px;color:var(--navy);font-weight:600}
.header-contact span{margin-left:10px;padding-left:10px;border-left:1px solid var(--line)}

.hero{position:absolute;left:0;top:80px;width:1200px;height:500px;background:linear-gradient(180deg,var(--sky-top) 0%,#5f97d6 45%,var(--sky-bottom) 100%)}
.hero-title{position:absolute;left:160px;top:300px;font-family:"Raleway",sans-serif;font-weight:500;font-size:40px;line-height:52px;color:var(--white)}

.about{position:absolute;left:0;top:580px;width:1200px;height:480px;background:var(--white)}
.about-visual{position:absolute;left:180px;top:40px;width:360px;height:260px;background:linear-gradient(135deg,#f4f5f7,#c9ced6);border-radius:4px}
.about-card{position:absolute;left:580px;top:150px;width:500px;height:250px;background:var(--white);border:1px solid #e3e6ea;box-shadow:0 4px 14px rgba(0,0,0,.12);padding:28px 32px}
.about-card h2{font-size:26px;font-weight:700;color:var(--navy);margin-bottom:14px}
.about-card p{font-size:13px;line-height:20px;color:var(--muted)}
.btn{display:inline-block;background:var(--blue);color:var(--white);font-size:12px;font-weight:600;letter-spacing:.5px;text-decoration:none;text-align:center}
.about-card .btn{position:absolute;right:32px;bottom:28px;width:110px;height:34px;line-height:34px}

.services{position:absolute;left:0;top:1060px;width:1200px;height:760px;background:var(--charcoal)}
.services h2{position:absolute;left:0;top:100px;width:1200px;text-align:center;font-size:26px;font-weight:600;color:#4b8fd8;letter-spacing:1px}
.service-list{position:absolute;left:210px;top:180px;width:780px;display:flex;justify-content:space-between}
.service-item{width:120px;text-align:center;color:var(--white);font-size:17px;line-height:22px}
.service-icon{width:64px;height:64px;margin:0 auto 10px;display:block}
.carousel{position:absolute;left:72px;top:380px;width:1056px;height:320px}
.slide{position:absolute;top:0;height:320px}
.slide-photo{position:absolute;left:0;top:0;width:100%;height:100%}
.photo-vault{background:linear-gradient(135deg,#6b4e35 0%,#a8845c 50%,#3e2e22 100%)}
.photo-guards{background:linear-gradient(135deg,#4a5a3c 0%,#8a9a78 50%,#2c3228 100%)}
.slide-label{position:absolute;left:0;bottom:0;width:100%;height:44px;line-height:44px;background:var(--blue);color:var(--white);font-weight:700;font-size:15px;text-align:center}
.slide-left{left:0;width:348px}
.slide-right{left:708px;width:348px}
.slide-center{left:356px;width:344px;background:var(--blue);color:var(--white);padding:26px 30px;text-align:center}
.slide-center h3{font-size:16px;font-weight:700;margin-bottom:14px}
.slide-center p{font-size:11.5px;line-height:17px;margin-bottom:12px}
.arrow{position:absolute;top:1590px;width:20px;height:30px}

.contact{position:absolute;left:0;top:1820px;width:1200px;height:468px;background:var(--white)}
.contact h2{position:absolute;left:0;top:50px;width:1200px;text-align:center;font-size:26px;font-weight:700;color:var(--navy)}
.contact-form{position:absolute;left:170px;top:130px;width:670px}
.field{position:absolute;font-size:11px;color:var(--ink)}
.field .input{border:1px solid var(--line);height:28px;margin-top:4px}
.field.msg .input{height:124px}
.form-note{position:absolute;left:0;top:156px;width:360px;font-size:10px;line-height:14px;color:var(--muted)}
.contact-form .btn{position:absolute;left:390px;top:176px;width:250px;height:30px;line-height:30px}
.contact-info{position:absolute;left:840px;top:130px;width:200px;height:280px;background:var(--blue);color:var(--white);padding:24px 20px;font-size:13px;line-height:20px}
.contact-info p{margin-bottom:16px}
.contact-info .btn{position:absolute;left:20px;bottom:20px;width:160px;height:34px;line-height:34px;background:var(--blue-dark)}

.site-footer{position:absolute;left:0;top:2288px;width:1200px;height:56px;background:var(--navy);color:#8fb0d8;font-size:11px}
.site-footer .copy{position:absolute;left:160px;top:20px}
.site-footer .links{position:absolute;right:160px;top:20px}
</style>
</head>
<body>

<header class="site-header">
  <div class="brand">
    <div class="brand-mark"></div>
    <div class="brand-name">SENTRAVIA SECURITY</div>
  </div>
  <nav class="main-nav">
    <a class="active" href="#">HOME</a>
    <a href="#">ABOUT US</a>
    <a href="#">OUR SERVICES</a>
    <a href="#">CONTACT US</a>
  </nav>
  <div class="header-contact">(+01) 555 0142<span>CHATTERLANE</span></div>
</header>

<section class="hero" role="img" aria-label="Blue sky with security cameras mounted on a pole">
  <h1 class="hero-title">Home Is Where You<br>Feel Safe!</h1>
</section>

<section class="about">
  <div class="about-visual" role="img" aria-label="White security camera on a wall mount"></div>
  <div class="about-card">
    <h2>ABOUT US</h2>
    <p>We protect commercial sites, construction projects and managed properties with smart camera systems, alarm monitoring and access control. Our team designs, installs and supports each solution so your people, assets and premises stay safe every hour of the day.</p>
    <a class="btn" href="#">SEE MORE</a>
  </div>
</section>

<section class="services">
  <h2>OUR SERVICES</h2>
  <div class="service-list">
    <div class="service-item">
      <svg class="service-icon" viewBox="0 0 64 64"><rect x="8" y="8" width="48" height="48" rx="4" fill="#3a3e44"/><rect x="16" y="24" width="26" height="12" rx="2" fill="#fff" transform="rotate(15 29 30)"/><path d="M40 34 L48 38 L44 44" stroke="#fff" stroke-width="3" fill="none"/></svg>
      CCTV<br>Service
    </div>
    <div class="service-item">
      <svg class="service-icon" viewBox="0 0 64 64"><rect x="8" y="8" width="48" height="48" rx="4" fill="#3a3e44"/><path d="M22 40 V30 a10 10 0 0 1 20 0 V40 Z" fill="#fff"/><rect x="19" y="40" width="26" height="4" fill="#fff"/><circle cx="32" cy="47" r="3" fill="#fff"/></svg>
      Security<br>Alarms
    </div>
    <div class="service-item">
      <svg class="service-icon" viewBox="0 0 64 64"><rect x="8" y="8" width="48" height="48" rx="4" fill="#3a3e44"/><rect x="22" y="16" width="20" height="32" rx="3" fill="none" stroke="#fff" stroke-width="3"/><circle cx="32" cy="28" r="4" fill="#fff"/><rect x="27" y="38" width="10" height="3" fill="#fff"/></svg>
      Access<br>Control
    </div>
    <div class="service-item">
      <svg class="service-icon" viewBox="0 0 64 64"><rect x="8" y="8" width="48" height="48" rx="4" fill="#3a3e44"/><path d="M32 14 C40 24 44 30 44 38 a12 12 0 0 1 -24 0 C20 32 26 28 28 22 C30 28 34 28 32 14 Z" fill="#fff"/></svg>
      Fire<br>Protection
    </div>
  </div>
  <div class="carousel">
    <div class="slide slide-left">
      <div class="slide-photo photo-vault" role="img" aria-label="Open bank vault door"></div>
      <div class="slide-label">BANKING SOLUTIONS</div>
    </div>
    <div class="slide slide-center">
      <h3>CCTV SERVICE</h3>
      <p>Closed circuit television (CCTV) has long been implemented by businesses as a surveillance tool in areas that need monitoring. With digital CCTV cameras, multiple video cameras transmit signals through a set of monitors. The cameras provide thorough surveillance of the area.</p>
      <p>With vast technological improvements over the last ten years, businesses with CCTV systems can use unique IP cameras and video analytics to monitor traffic flows, people-count and more.</p>
    </div>
    <div class="slide slide-right">
      <div class="slide-photo photo-guards" role="img" aria-label="Security officers escorting a client outdoors"></div>
      <div class="slide-label">PERSONAL SECURITY</div>
    </div>
  </div>
</section>
<svg class="arrow" style="left:34px" viewBox="0 0 20 30"><path d="M16 3 L4 15 L16 27" stroke="#fff" stroke-width="3" fill="none"/></svg>
<svg class="arrow" style="left:1146px" viewBox="0 0 20 30"><path d="M4 3 L16 15 L4 27" stroke="#fff" stroke-width="3" fill="none"/></svg>

<section class="contact">
  <h2>CONTACT US:</h2>
  <form class="contact-form">
    <div class="field" style="left:0;top:0;width:180px">Full Name*<div class="input"></div></div>
    <div class="field" style="left:190px;top:0;width:180px">Company*<div class="input"></div></div>
    <div class="field" style="left:0;top:52px;width:180px">Email Address*<div class="input"></div></div>
    <div class="field" style="left:190px;top:52px;width:180px">State<div class="input"></div></div>
    <div class="field" style="left:0;top:104px;width:180px">Phone Number*<div class="input"></div></div>
    <div class="field" style="left:190px;top:104px;width:180px">Postcode<div class="input"></div></div>
    <div class="field msg" style="left:390px;top:0;width:250px">Message<div class="input"></div></div>
    <p class="form-note">Fields marked with * are required. We reply within one business day.</p>
    <a class="btn" href="#">SEND MESSAGE</a>
  </form>
  <aside class="contact-info">
    <p>(+01) 555 0142<br>(+01) 555 0187</p>
    <p>info@sentravia.example<br>North Harbour<br>Mon to Fri</p>
    <a class="btn" href="#">CHATTERLANE</a>
  </aside>
</section>

<footer class="site-footer">
  <div class="copy">copyright Sentravia</div>
  <div class="links">Terms | Privacy</div>
</footer>

</body>
</html>
```